Brivtel sales folder inserts

We need the same design for 4 separate service offerings to put inside our sales folder. Each insert should be laid out the same with different images and text and the 2nd, 3rd, and 4th should each be 3/4" shorter than the previous one so that when all 4 are inserted into the folder you see the black strip with text showing what the service offering is. Basically staggered inserts.

Industry/Entity Type

Information Technology

Font styles to use
Sans Serif

Colors
acd136

Requirements
Must have
• Brivtel logo and included text. Keep with the green Pantone 90 and black color scheme
Nice to have
• a better layout and pics

```html
<!DOCTYPE html>
<html lang="en">
<head>
<meta charset="utf-8">
<title>Brivtel sales folder inserts</title>
<link rel="stylesheet" href="https://fonts.googleapis.com/css2?family=Russo+One&family=Montserrat:wght@400;600;700&display=swap">
<style>
:root{
  --green:#acd136;
  --green-deep:#8fb325;
  --black:#231f20;
  --white:#ffffff;
  --paper:#fbfbfb;
  --ink:#444444;
  --stage:#dcdcdc;
  --heading:"Russo One", "Arial Black", sans-serif;
  --body:"Montserrat", Arial, sans-serif;
}
*{box-sizing:border-box;margin:0;padding:0}
html,body{width:1200px;height:2400px;overflow:hidden}
body{background:var(--stage);position:relative;font-family:var(--body);color:var(--ink)}

.insert{position:absolute;width:520px;background:var(--paper);box-shadow:0 4px 14px rgba(0,0,0,.18);overflow:hidden}
.insert--business{left:60px;top:230px;height:736px}
.insert--it{left:620px;top:230px;height:782px}
.insert--secure{left:60px;top:1200px;height:832px}
.insert--voice{left:620px;top:1200px;height:872px}

.brand{position:absolute;left:40px;top:36px;display:flex;align-items:center;gap:12px}
.brand__mark{width:44px;height:44px;background:var(--green)}
.brand__name{font-family:var(--heading);font-size:22px;letter-spacing:2px;color:var(--black);border-left:2px solid var(--black);padding-left:12px;line-height:44px}

.tab{position:absolute;left:299px;top:15px;width:221px;height:84px;background:var(--black);border-top-right-radius:22px;display:flex;align-items:center;justify-content:flex-end;padding-right:42px}
.tab__title{font-family:var(--heading);font-weight:400;font-size:26px;line-height:26px;color:var(--white);text-align:right;letter-spacing:.5px}
.spine{position:absolute;left:485px;top:60px;width:35px;height:312px;background:var(--black)}

.hero{position:absolute;left:6px;top:108px;width:479px;height:264px;background:var(--green);border-radius:36px 0 0 36px;padding:20px 0 17px 21px}
.hero__photo{width:100%;height:100%;border-radius:26px 0 0 26px;background:
  radial-gradient(ellipse 120px 70px at 70px 200px,#1f2a3f 0%,#34445d 55%,rgba(52,68,93,0) 100%),
  radial-gradient(ellipse 120px 60px at 20px 180px,#c98d6a 0%,rgba(201,141,106,0) 100%),
  linear-gradient(200deg,#f4f7fa 0%,#dfe7ee 45%,#c2ceda 100%)}
.hero__line{position:absolute;right:22px;bottom:42px;text-align:right;font-family:var(--heading);font-size:21px;line-height:25px}
.hero__line .g{color:var(--green-deep)}
.hero__line .k{color:var(--black)}
.hero__inset{position:absolute;right:0;bottom:0;width:176px;height:108px;background:linear-gradient(160deg,#e9eef4,#9aa9bb)}

.cols{position:absolute;left:43px;top:395px;right:30px;display:flex;gap:44px}
.col{flex:1;display:flex;flex-direction:column;gap:9px}
.col--left{flex:0 0 208px}
.col__head{font-family:var(--heading);font-size:10px;line-height:12px;color:var(--black);margin-top:2px}
.col__head span{display:block;color:var(--green-deep)}
.col__head .inline{display:inline}
.col p{font-size:6.6px;line-height:8.6px}
.col--voice p{font-size:7.4px;line-height:9.6px}
.list{list-style:none;display:flex;flex-direction:column;gap:4px}
.list li{position:relative;padding-left:13px;font-size:6.6px;line-height:8.4px}
.list li::before{content:"";position:absolute;left:0;top:1px;width:7px;height:6px;background:var(--green);border-radius:1px}
.list b{font-weight:700;color:var(--black)}
.list--bold li{font-weight:600;color:var(--black);padding-top:2px;padding-bottom:2px}
.list--roomy{gap:7px}

.pic{border-radius:2px}
.pic--lock{width:98px;height:70px;flex:0 0 98px;background:linear-gradient(135deg,#0c2640,#2c6b96)}
.pic--team{width:92px;height:66px;background:linear-gradient(160deg,#5a7fa6,#1b2e4a)}
.pic--blocks{width:88px;height:66px;background:linear-gradient(135deg,#bfe3f2,#e7f3f9)}
.pic--laptop{width:140px;height:96px;margin:8px auto;background:linear-gradient(180deg,#f1f3f6 0,#f1f3f6 82%,#8a8d92 82%)}
.pic--compass{width:196px;height:134px;margin:4px auto;background:radial-gradient(circle at 60% 55%,#3d80a8,#0d1b2a 70%)}
.pic--cams{width:124px;height:54px;margin:6px auto;background:linear-gradient(180deg,#e6e6e6,#8f9298)}
.pic--options{width:178px;height:178px;margin:6px auto;background:radial-gradient(circle at 50% 40%,#6b5a4c,#2f2620 70%)}
.pic--question{width:120px;height:96px;margin:8px auto;background:radial-gradient(circle at 50% 45%,#f3d9da,#c94b4f 60%,#eeeeee 62%)}
.row{display:flex;gap:10px;align-items:flex-start}
.row p{flex:1}
.row--pics{margin-top:6px}
.col--offset{padding-top:28px}

.strap{position:absolute;right:0;bottom:0;width:255px;min-height:40px;background:var(--black);border-top-left-radius:20px;color:var(--white);font-family:var(--body);font-weight:700;font-size:8.2px;line-height:10px;display:flex;align-items:center;justify-content:center;text-align:center;padding:6px 14px}
.baseline{position:absolute;left:0;bottom:0;width:270px;height:5px;background:var(--green)}
</style>
</head>
<body>

<article class="insert insert--business">
  <div class="brand"><span class="brand__mark"></span><span class="brand__name">BRIVTEL</span></div>
  <div class="spine"></div>
  <div class="tab"><h2 class="tab__title">TOTAL<br>BUSINESS</h2></div>
  <div class="hero">
    <div class="hero__photo" role="img" aria-label="Hand on a computer mouse in front of a bright monitor"></div>
    <p class="hero__line"><span class="g">RUN ANYWHERE</span><br><span class="k">PROTECT ANYTHING</span></p>
  </div>
  <div class="cols">
    <section class="col col--left">
      <h3 class="col__head">YOUR BUSINESS<span>CONTINUITY SOLUTION.</span></h3>
      <p>Brivtel's TOTAL-BUSINESS solution provides comprehensive backups for your data like never before.</p>
      <p>In todays environment threats are never ending. There is always a new threat trying to get to your data, whether to Vaultlock it and hold it for ransom, or be malicious and delete it for no reason at all.</p>
      <div class="row">
        <div class="pic pic--lock" role="img" aria-label="Digital padlock on a blue circuit background"></div>
        <p>Keeping your network up to date and monitoring for suspicious activity are all recommended actions, but backing up your data is the most important action you can take.</p>
      </div>
      <p>Don't just back up your data. Verify it. What good is a backup of your data if it does not work when you need it. The Brivtel TOTAL-Business solution tests and verifies your data on a daily basis.</p>
      <p>The TOTAL-Business solution also provides you a local and an off-site copy of your data. What good is a business continuity plan if your backups burn down with your building.</p>
      <p>The TOTAL-Business solution provides an onsite server resource should you need it, as well as allowing you to spin up virtual servers in the cloud during a disaster scenario.</p>
    </section>
    <section class="col">
      <h3 class="col__head">DOES YOUR BACKUP<span>SOLUTION DO THIS?</span></h3>
      <ul class="list">
        <li>Test and verify your backups by booting on a virtual server in the cloud</li>
        <li>Backup your CloudDesk 360</li>
        <li>Allow you to spin up virtual servers in the cloud during a disaster</li>
      </ul>
      <h3 class="col__head">DID YOU <span class="inline">KNOW?</span></h3>
      <ul class="list">
        <li><b>60%</b> of backups are incomplete</li>
        <li><b>50%</b> of restores fail</li>
        <li><b>40%</b> of the SMB market will be attacked by a hacker, 50% wont even know it</li>
        <li><b>20%</b> of SMB market will lose critical data every 5-years</li>
        <li><b>90%</b> of business that lost data for 10-days or more filed for bankruptcy immediately</li>
      </ul>
      <div class="row row--pics">
        <div class="pic pic--team" role="img" aria-label="Person working at a glowing backup interface"></div>
        <div class="pic pic--blocks" role="img" aria-label="Letter blocks spelling backup and data"></div>
      </div>
    </section>
  </div>
  <div class="baseline"></div>
  <footer class="strap">A LITTLE MISTAKE CAN COST A FORTUNE</footer>
</article>

<article class="insert insert--it">
  <div class="brand"><span class="brand__mark"></span><span class="brand__name">BRIVTEL</span></div>
  <div class="spine"></div>
  <div class="tab"><h2 class="tab__title">TOTAL–IT</h2></div>
  <div class="hero">
    <div class="hero__photo" role="img" aria-label="Hand on a computer mouse in front of a bright monitor"></div>
    <div class="hero__inset" role="img" aria-label="Calculator and financial charts on a desk"></div>
  </div>
  <div class="cols">
    <section class="col col--left">
      <h3 class="col__head">A TRUE IT<span>PARTNERSHIP</span></h3>
      <p>An IT partner not provider. We understand why your critical business services are so important to your daily operations. This is why we spend so much time aligning our technology support with just such business services. Building a program that relies on 24x7x365 network monitoring coupled with an aggressive preventative maintenance component to ensure optimum uptime for your business.</p>
      <div class="pic pic--laptop" role="img" aria-label="Laptop showing a network monitoring dashboard"></div>
      <p>One of the major challenges in maintaining a computer network is trying to predict what will fail and when. With our TOTAL-IT solution, we can prevent many network failures from ever happening. By combining regular and comprehensive preventative maintenance and robust real-time monitoring of your critical network and desktop devices, we ensure the reliability and stability of your IT assets.</p>
      <p>This solution is so effective, our customers see almost immediate results. A regularly maintained network means fewer failures, yielding higher productivity and savings on support costs for you.</p>
      <p>At the same time, your exposure to security risks is dramatically lessened, and frustration from unstable IT resources almost vanishes. We allow our customers to focus on their core business functions by taking the worry out of owning a computer network.</p>
    </section>
    <section class="col col--offset">
      <h3 class="col__head">DO THESE ISSUES<span>PLAGUE YOUR BUSINESS?</span></h3>
      <ul class="list">
        <li><b>Network neglected?</b><br>Is yours perceived as a "necessary evil" and not as integral to improving business performance?</li>
        <li><b>Downtime impact?</b><br>Are IT outages distracting your staff from their core focus, or prohibiting them from working efficiently?</li>
        <li><b>Distracted employees?</b><br>Do your staff rely on other non-IT employees to deal with distracting IT problems?</li>
      </ul>
      <h3 class="col__head">PROGRAM <span class="inline">ADVANTAGES:</span></h3>
      <ul class="list">
        <li><b>Increased productivity:</b><br>Continuous insight into your network lets us reduce the business impact of IT failure by shortening the time from network failure to issue resolution.</li>
        <li><b>Reduced business impact from IT failures:</b><br>Combining preventative maintenance and remote monitoring means we minimize failures that could impact your business. Your network behaves in a stable and reliable manner.</li>
        <li><b>Reduced network downtime through proactive maintenance:</b><br>Through regular, preventative maintenance activities designed to keep your network operating efficiently, we reduce the number of emergency incidents you encounter.</li>
      </ul>
    </section>
  </div>
  <div class="baseline"></div>
  <footer class="strap">STOP BUYING DOWNTIME – INVEST IN UPTIME</footer>
</article>

<article class="insert insert--secure">
  <div class="brand"><span class="brand__mark"></span><span class="brand__name">BRIVTEL</span></div>
  <div class="spine"></div>
  <div class="tab"><h2 class="tab__title">TOTAL<br>SECURE</h2></div>
  <div class="hero">
    <div class="hero__photo" role="img" aria-label="Hand on a computer mouse in front of a bright monitor"></div>
    <p class="hero__line"><span class="k">TOTAL–SECURE</span><br><span class="g">SECURITY AT ITS BEST</span></p>
  </div>
  <div class="cols">
    <section class="col col--left">
      <h3 class="col__head">TOTAL–SECURE PROVIDES<span>PIECE OF MIND.</span></h3>
      <p>Secure your company with industry leading cameras and door access systems. Monitor your business like you monitor your accounts.</p>
      <div class="pic pic--compass" role="img" aria-label="Compass dial pointing from risk to security"></div>
      <p>Brivtel provides network video recorders and IP-CCTV cameras with intelligence. Keeping an eye on your business 24X7 is essential in todays environment. Whether the problem is shrinking inventory, unauthorized access, or performance, keeping an eye on things is essential.</p>
      <p>Having the ability to go back in time and review what happened is becoming more important by the day. Having a video of an incident can mean the difference between settling out of court or dismissing of the case entirely.</p>
      <p>Securing your entry points to your site is crucial. With a card access system from Brivtel you will have control of who has access and when. You will have the ability to control ingress and egress to specific areas. Never have to worry about lost keys, with card access you delete the card and your secure.</p>
    </section>
    <section class="col">
      <h3 class="col__head">DO I NEED THESE<span>TYPES OF SYSTEMS?</span></h3>
      <ul class="list">
        <li><b>I use hard keys?</b><br>Hard keys can be lost, copied, and not returned. Card access provides you control over these problems.</li>
        <li><b>I trust my people, I don't need to have video cameras?</b><br>This is not a matter of trust, it is a matter of security. You can allow employees access to viewing certain cameras to provide a level of security.</li>
        <li><b>This sounds complicated?</b><br>Brivtel can provide complete management of these systems so you never have to wonder how this works. A single call gets it all done now, call Brivtel.</li>
      </ul>
      <h3 class="col__head">WHAT CAN I DO<span>WITH THESE SYSTEMS?</span></h3>
      <ul class="list list--bold">
        <li>Receive alerts according to events</li>
        <li>Review events of the past</li>
        <li>Increase security with access events</li>
        <li>Enhanced reporting capabilities</li>
        <li>View video from anywhere</li>
        <li>End lost or copied keys</li>
        <li>Provide employees piece of mind</li>
        <li>24X7 On Call Services</li>
      </ul>
      <div class="pic pic--cams" role="img" aria-label="Security cameras and a card access keypad"></div>
    </section>
  </div>
  <div class="baseline"></div>
  <footer class="strap">STOP BUYING DOWNTIME – INVEST IN UPTIME</footer>
</article>

<article class="insert insert--voice">
  <div class="brand"><span class="brand__mark"></span><span class="brand__name">BRIVTEL</span></div>
  <div class="spine"></div>
  <div class="tab"><h2 class="tab__title">TOTAL<br>VOICE</h2></div>
  <div class="hero">
    <div class="hero__photo" role="img" aria-label="Hand on a computer mouse in front of a bright monitor"></div>
    <p class="hero__line"><span class="k">TOTAL–VOICE</span><br><span class="g">EVERY OPTION</span></p>
  </div>
  <div class="cols">
    <section class="col col--left col--voice">
      <h3 class="col__head">TOTAL–VOICE PROVIDES<span>ENDLESS OPTIONS.</span></h3>
      <p>Working with Brivtel provides you with options. We work with every provider so you can select the best option for your needs.</p>
      <div class="pic pic--options" role="img" aria-label="Businessman pointing at five green option circles"></div>
      <p>Brivtel offers both On-Premise Unified Communication solutions and Hosted Unified Communication solutions.</p>
      <p>No matter what your need is Brivtel has the solution with our TOTAL-Voice program.</p>
      <p>Brivtel has relationships with almost every provider for internet and voice connections for your business.</p>
      <p>We can provide quotes from any provider in the area.</p>
      <p>More options can mean larger savings. You will have the information to make the best selection for your business needs.</p>
    </section>
    <section class="col">
      <h3 class="col__head">HOW CAN<span>BRIVTEL ASSIST?</span></h3>
      <ul class="list list--bold list--roomy">
        <li>Provide multiple options for review</li>
        <li>Provide cost savings</li>
        <li>Educate client on options</li>
        <li>Locate possible cost over runs on existing provider solutions</li>
        <li>Provide turn key solutions</li>
        <li>Provide On-Premise Solutions</li>
        <li>Provide Hosted Solutions</li>
        <li>Multi-site and remote worker solutions</li>
        <li>Contact center solutions</li>
        <li>Multi media Contact Center Solutions</li>
        <li>Advance Reporting and Monitoring</li>
      </ul>
      <div class="pic pic--question" role="img" aria-label="Speech bubble asking what should I do"></div>
    </section>
  </div>
  <div class="baseline"></div>
  <footer class="strap">GIVE YOURSELF OPTIONS, AND WE CAN HELP YOU CHOOSE THE RIGHT OPTION</footer>
</article>

</body>
</html>
```